Name and logo for Ember Fitness Coaching LLC
Ember Fitness Coaching
Name and logo for Ember Fitness Coaching LLC - Health
Creative Brief
Simple
Dale Whitmore
Owner
Larkmont, CO
dale@emberfitnesscoaching-example.com
emberfitnesscoaching-example.com

```html
<!DOCTYPE html>
<html lang="en">
<head>
<meta charset="utf-8">
<title>Ember Fitness Coaching – Business Card Options</title>
<link href="https://fonts.googleapis.com/css2?family=Arimo&family=Barlow:wght@300;400;600&display=swap" rel="stylesheet">
<style>
  :root {
    --page: #ffffff;
    --navy: #27306a;
    --navy-deep: #1d2454;
    --frame: #c9c9c9;
    --ink: #111111;
    --light: #ffffff;
    --soft: #c9cde6;
    --divider: #6c6cf0;
  }
  * { margin: 0; padding: 0; box-sizing: border-box; }
  html, body { width: 1200px; height: 818px; overflow: hidden; background: var(--page); }
  body { position: relative; font-family: "Barlow", sans-serif; color: var(--light); }

  .section-title {
    position: absolute; left: 0; width: 1200px; text-align: center;
    font-family: "Arimo", sans-serif; font-size: 38px; font-weight: 400; color: var(--ink);
  }
  .section-title.dual { top: 28px; }
  .section-title.single { top: 728px; }
  .divider-line {
    position: absolute; left: 0; top: 408px; width: 1200px;
    border-top: 2px dashed var(--divider);
  }

  .frame { position: absolute; background: var(--frame); }
  .card { position: absolute; background: var(--navy); overflow: hidden; }

  .wordmark { position: absolute; line-height: 1; }
  .wordmark .name { font-weight: 400; letter-spacing: -1px; color: var(--light); }
  .wordmark .tagline {
    display: block; font-weight: 400; color: var(--soft);
    text-transform: uppercase; text-align: right;
  }

  .contact-row { position: absolute; display: flex; align-items: center; }
  .contact-row svg { flex: none; }
  .contact-row .detail { color: var(--soft); font-size: 11px; line-height: 1.35; margin-left: 14px; white-space: nowrap; }
  .contact-row .detail.small { font-size: 7.5px; line-height: 1.5; }
  .rule { position: absolute; height: 2px; background: var(--light); opacity: .85; }

  .person-name { position: absolute; line-height: 1; white-space: nowrap; }
  .person-role { position: absolute; font-size: 12px; color: var(--soft); }

  .name-plate { position: absolute; background: var(--navy-deep); }
</style>
</head>
<body>

<h1 class="section-title dual">Dual Side</h1>

<!-- Dual side: front -->
<section class="card" style="left:108px; top:108px; width:475px; height:259px;">
  <div class="wordmark" style="left:146px; top:90px;">
    <span class="name" style="font-size:60px;">Ember</span>
    <span class="tagline" style="font-size:12px; letter-spacing:3px; margin-top:6px;">Fitness Coaching</span>
  </div>
</section>

<!-- Dual side: back -->
<div class="frame" style="left:629px; top:113px; width:477px; height:254px;"></div>
<section class="card" style="left:648px; top:132px; width:444px; height:218px;">
  <div class="person-name" style="left:20px; top:70px;">
    <div style="font-size:30px; font-weight:300;">Dale</div>
    <div style="font-size:32px; font-weight:600;">Whitmore</div>
  </div>
  <div class="person-role" style="left:20px; top:150px;">Owner</div>

  <div class="contact-row" style="left:247px; top:42px;">
    <svg width="26" height="26" viewBox="0 0 24 24" fill="none" stroke="#fff" stroke-width="1.6"><path d="M5 3h4l2 5-2.5 1.5a11 11 0 0 0 6 6L16 13l5 2v4a2 2 0 0 1-2 2A17 17 0 0 1 3 5a2 2 0 0 1 2-2z"/></svg>
    <span class="detail">555-201-4477</span>
  </div>
  <div class="rule" style="left:240px; top:88px; width:194px;"></div>
  <div class="contact-row" style="left:247px; top:101px;">
    <svg width="26" height="26" viewBox="0 0 24 24" fill="none" stroke="#fff" stroke-width="1.6"><circle cx="12" cy="12" r="10"/><circle cx="12" cy="10" r="3.5"/><path d="M5.5 19a8 8 0 0 1 13 0"/></svg>
    <span class="detail small">dale@emberfitnesscoaching-example.com<br>emberfitnesscoaching-example.com</span>
  </div>
  <div class="rule" style="left:240px; top:146px; width:194px;"></div>
  <div class="contact-row" style="left:247px; top:159px;">
    <svg width="26" height="26" viewBox="0 0 24 24" fill="none" stroke="#fff" stroke-width="1.6"><path d="M12 22s7-7 7-12a7 7 0 0 0-14 0c0 5 7 12 7 12z"/><circle cx="12" cy="10" r="2.5"/></svg>
    <span class="detail">Larkmont, CO</span>
  </div>
</section>

<div class="divider-line"></div>

<!-- Single side: name plate variant -->
<section class="card" style="left:108px; top:425px; width:475px; height:271px;">
  <div class="wordmark" style="left:32px; top:57px;">
    <span class="name" style="font-size:48px;">Ember</span>
    <span class="tagline" style="font-size:9px; letter-spacing:2.5px; margin-top:5px;">Fitness Coaching</span>
  </div>
  <div class="name-plate" style="left:0; top:182px; width:211px; height:55px;"></div>
  <div class="person-name" style="left:18px; top:192px; font-size:20px; font-weight:400;">Dale Whitmore</div>
  <div class="person-role" style="left:18px; top:217px; font-size:11px;">Owner</div>

  <div class="contact-row" style="left:258px; top:60px;">
    <svg width="26" height="26" viewBox="0 0 24 24" fill="none" stroke="#fff" stroke-width="1.6"><path d="M5 3h4l2 5-2.5 1.5a11 11 0 0 0 6 6L16 13l5 2v4a2 2 0 0 1-2 2A17 17 0 0 1 3 5a2 2 0 0 1 2-2z"/></svg>
    <span class="detail">555-201-4477</span>
  </div>
  <div class="rule" style="left:247px; top:106px; width:207px;"></div>
  <div class="contact-row" style="left:258px; top:125px;">
    <svg width="26" height="26" viewBox="0 0 24 24" fill="none" stroke="#fff" stroke-width="1.6"><circle cx="12" cy="12" r="10"/><circle cx="12" cy="10" r="3.5"/><path d="M5.5 19a8 8 0 0 1 13 0"/></svg>
    <span class="detail small">dale@emberfitnesscoaching-example.com<br>emberfitnesscoaching-example.com</span>
  </div>
  <div class="rule" style="left:247px; top:168px; width:207px;"></div>
  <div class="contact-row" style="left:258px; top:190px;">
    <svg width="26" height="26" viewBox="0 0 24 24" fill="none" stroke="#fff" stroke-width="1.6"><path d="M12 22s7-7 7-12a7 7 0 0 0-14 0c0 5 7 12 7 12z"/><circle cx="12" cy="10" r="2.5"/></svg>
    <span class="detail">Larkmont, CO</span>
  </div>
</section>

<!-- Single side: framed variant -->
<div class="frame" style="left:629px; top:425px; width:477px; height:271px;"></div>
<section class="card" style="left:648px; top:444px; width:444px; height:233px;">
  <div class="wordmark" style="left:24px; top:36px;">
    <span class="name" style="font-size:48px;">Ember</span>
    <span class="tagline" style="font-size:9px; letter-spacing:2.5px; margin-top:5px;">Fitness Coaching</span>
  </div>
  <div class="person-name" style="left:24px; top:152px; font-size:20px;"><span style="font-weight:600;">Dale</span> <span style="font-weight:400;">Whitmore</span></div>
  <div class="rule" style="left:24px; top:176px; width:46px;"></div>
  <div class="person-role" style="left:24px; top:184px; font-size:11px;">Owner</div>

  <div class="contact-row" style="left:247px; top:44px;">
    <svg width="26" height="26" viewBox="0 0 24 24" fill="none" stroke="#fff" stroke-width="1.6"><path d="M5 3h4l2 5-2.5 1.5a11 11 0 0 0 6 6L16 13l5 2v4a2 2 0 0 1-2 2A17 17 0 0 1 3 5a2 2 0 0 1 2-2z"/></svg>
    <span class="detail">555-201-4477</span>
  </div>
  <div class="rule" style="left:240px; top:89px; width:194px;"></div>
  <div class="contact-row" style="left:247px; top:105px;">
    <svg width="26" height="26" viewBox="0 0 24 24" fill="none" stroke="#fff" stroke-width="1.6"><circle cx="12" cy="12" r="10"/><circle cx="12" cy="10" r="3.5"/><path d="M5.5 19a8 8 0 0 1 13 0"/></svg>
    <span class="detail small">dale@emberfitnesscoaching-example.com<br>emberfitnesscoaching-example.com</span>
  </div>
  <div class="rule" style="left:240px; top:146px; width:194px;"></div>
  <div class="contact-row" style="left:247px; top:161px;">
    <svg width="26" height="26" viewBox="0 0 24 24" fill="none" stroke="#fff" stroke-width="1.6"><path d="M12 22s7-7 7-12a7 7 0 0 0-14 0c0 5 7 12 7 12z"/><circle cx="12" cy="10" r="2.5"/></svg>
    <span class="detail">Larkmont, CO</span>
  </div>
</section>

<h2 class="section-title single">Single Side</h2>

</body>
</html>
```